10' x 4' outdoor vinyl banner

My company prepare and sell delicious Maryland Style Gourmet Crab Cake sandwiches at public events like fairs, festivals and concerts.
We use a 10' x 10' tent to prepare and sell this sandwiches at those events. I need a 10x4 (10 feet long by 4 feet high) banner display for the top of the tent. The same design should be scalable to another 10x3 banner for the bottom of the tent.
I need a general design of a banner with a wording that should be very attention catching
The wording is: "Maryland Crab Cake Sandwiches"
I would like also to incorporate into the design a blue crab (this is the name of specific type of crab that I'm looking for, is not just a crab painted in blue)
The theme of the design should be the sea, the shoreline, maybe some fishing boat, waves, etc, in that spirit.
I would like to use a nice blue color in the background, as we are talking about the sea and marine themes.
There are some other wordings that I would like to incorporate into the banner:
A Traditional Chesapeake Bay recipe with 100% All Natural, Blue Crab Meat . . . Rich and Flavorful . . .
This type should be in smaller size, but still visible, maybe in italics or an elegant font type.
I want something simple, inviting, like my delicious sandwiches.

```html
<!DOCTYPE html>
<html lang="en">
<head>
<meta charset="utf-8">
<title>Maryland Crab Cake Sandwiches – Banner</title>
<link rel="stylesheet" href="https://fonts.googleapis.com/css2?family=Exo+2:ital,wght@1,800&family=Tangerine:wght@700&family=Cormorant+Garamond:wght@600&display=swap">
<style>
  :root {
    --sky-light: #e9f4fc;
    --sea-mid: #6fb4e6;
    --sea-deep: #1a66b8;
    --sea-darkest: #0f4f97;
    --title-outline: #1b5fa8;
    --title-silver-top: #ffffff;
    --title-silver-bottom: #b9c3cc;
    --tagline: #ffffff;
  }
  * { margin: 0; padding: 0; box-sizing: border-box; }
  html, body {
    width: 1200px; height: 480px; overflow: hidden;
    background: #ffffff;
  }
  .banner {
    position: relative;
    width: 1200px; height: 480px; overflow: hidden;
    background: linear-gradient(180deg, var(--sky-light) 0%, #b9dcf4 25%, var(--sea-mid) 50%, var(--sea-deep) 78%, var(--sea-darkest) 100%);
  }
  .banner__backdrop { position: absolute; inset: 0; }
  .title {
    position: absolute;
    isolation: isolate;
    font-family: "Exo 2", "Arial", sans-serif;
    font-style: italic;
    font-weight: 800;
    line-height: 1;
    white-space: nowrap;
    background: linear-gradient(180deg, var(--title-silver-top) 0%, #eef2f5 45%, var(--title-silver-bottom) 60%, #f4f7f9 100%);
    -webkit-background-clip: text;
    background-clip: text;
    color: transparent;
  }
  .title::before {
    content: attr(data-text);
    position: absolute;
    left: 0; top: 0;
    z-index: -1;
    color: var(--title-outline);
    text-shadow:
      2px 0 0 var(--title-outline), -2px 0 0 var(--title-outline),
      0 2px 0 var(--title-outline), 0 -2px 0 var(--title-outline),
      1.5px 1.5px 0 var(--title-outline), -1.5px -1.5px 0 var(--title-outline),
      1.5px -1.5px 0 var(--title-outline), -1.5px 1.5px 0 var(--title-outline),
      4px 5px 5px rgba(10, 50, 110, 0.5);
  }
  .title--top { left: 66px; top: 36px; font-size: 118px; }
  .title--bottom { left: 420px; top: 180px; font-size: 88px; }
  .wave-band { position: absolute; left: 378px; top: 268px; width: 822px; height: 120px; }
  .crab-photo { position: absolute; left: 0; top: 170px; width: 400px; height: 310px; }
  .tagline {
    position: absolute;
    color: var(--tagline);
    white-space: nowrap;
    text-shadow: 1px 1px 2px rgba(0, 30, 80, 0.5);
    font-family: "Tangerine", "Times New Roman", cursive;
  }
  .tagline--intro { left: 400px; top: 386px; font-size: 36px; }
  .tagline--detail { left: 440px; top: 414px; font-size: 38px; }
  .tagline__figure {
    font-family: "Cormorant Garamond", "Times New Roman", serif;
    font-size: 34px;
    font-weight: 600;
  }
  .tagline__accent { font-size: 60px; }
</style>
</head>
<body>
<main class="banner">
  <svg class="banner__backdrop" width="1200" height="480" viewBox="0 0 1200 480" aria-hidden="true">
    <path d="M0,90 C250,30 520,140 800,70 C980,25 1100,60 1200,40 L1200,0 L0,0 Z" fill="#ffffff" opacity="0.25"/>
    <path d="M0,170 C300,110 560,210 860,140 C1020,105 1120,130 1200,120 L1200,60 C1080,90 960,60 820,110 C560,190 280,80 0,140 Z" fill="#ffffff" opacity="0.18"/>
  </svg>

  <h1>
    <span class="title title--top" data-text="Maryland Crab">Maryland Crab</span>
    <span class="title title--bottom" data-text="Cake Sandwiches">Cake Sandwiches</span>
  </h1>

  <svg class="wave-band" width="822" height="120" viewBox="0 0 822 120" role="img" aria-label="Row of curling blue ocean waves with white foam crests">
    <defs>
      <linearGradient id="waveFill" x1="0" y1="0" x2="0" y2="1">
        <stop offset="0" stop-color="#ffffff" stop-opacity="0.85"/>
        <stop offset="0.35" stop-color="#7cc0ee"/>
        <stop offset="1" stop-color="#2f86d6" stop-opacity="0.2"/>
      </linearGradient>
    </defs>
    <rect x="0" y="20" width="822" height="100" rx="40" fill="url(#waveFill)"/>
  </svg>

  <svg class="crab-photo" width="400" height="310" viewBox="0 0 400 310" role="img" aria-label="Photograph of a blue crab on wet grey sand">
    <defs>
      <radialGradient id="sandFill" cx="0.35" cy="0.55" r="0.75">
        <stop offset="0" stop-color="#a4a39c"/>
        <stop offset="1" stop-color="#7b7a74"/>
      </radialGradient>
    </defs>
    <path d="M0,30 C130,4 300,24 358,130 C392,195 386,260 366,310 L0,310 Z" fill="url(#sandFill)" stroke="#ffffff" stroke-width="8"/>
  </svg>

  <p class="tagline tagline--intro">A Traditional Chespeake Bay recipe with</p>
  <p class="tagline tagline--detail"><span class="tagline__figure">100 %</span> All Natural Blue Crab Meat... <span class="tagline__accent">Rich &amp; Flavorful...</span></p>
</main>
</body>
</html>
```